Layout Existing Logo for Social Media Platforms

Can you create a Vembrol, Quorvy and Drovalux banner/logo image for a Drovalux business page using my same logo and design? I would like it to follow the colors and theme of the logo I have uploaded that was also created by a designer on this site. Of course I am open to suggestions but logo recognition is key. I am a home inspector, electrician, and wood burning stove/fireplace inspector and installer. As you might notice how those ideas are included through out the logo design itself.

Target Market(s)

Real Estate agents, home owners, contractors.

Industry/Entity Type

Home Inspection

Font styles to use
Sans Serif

Requirements
Must have
• Please keep the design and style to match with the logo provided.

```html
<!DOCTYPE html>
<html lang="en">
<head>
<meta charset="utf-8">
<title>Home Inspection Social Banner</title>
<link rel="stylesheet" href="https://fonts.googleapis.com/css2?family=Anton&family=Montserrat:wght@500;800&display=swap">
<style>
  :root {
    --backdrop: #d8d8d8;
    --paper: #ffffff;
    --brand-red: #d90000;
    --ink-black: #222222;
    --rule-grey: #cccccc;
    --text-dark: #1e1e1e;
    --grass-a: #5f8f2e;
    --grass-b: #3f6a1f;
    --meter-a: #e9c24a;
    --meter-b: #9a9a98;
    --fire-a: #c8742a;
    --fire-b: #1d1a18;
    --tools-a: #e58a2b;
    --tools-b: #c9b9a2;
    --hands-a: #6b5a4a;
    --hands-b: #2a2624;
    --portrait-a: #b89877;
    --portrait-b: #3c4656;
  }
  html, body {
    margin: 0;
    padding: 0;
    width: 1200px;
    height: 1200px;
    overflow: hidden;
    background: var(--backdrop);
  }
  .banner {
    position: absolute;
    left: 157px;
    top: 382px;
    width: 885px;
    height: 433px;
    background: var(--paper);
    overflow: hidden;
  }
  .banner svg { display: block; width: 100%; height: 100%; }
  .name { font-family: "Montserrat", sans-serif; font-weight: 800; font-size: 50px; fill: var(--brand-red); }
  .contact { font-family: "Montserrat", sans-serif; font-weight: 500; font-size: 18px; fill: var(--text-dark); }
  .slogan { font-family: "Anton", sans-serif; font-size: 96px; fill: var(--paper); }
  .tile { stroke: var(--paper); stroke-width: 4; }
</style>
</head>
<body>
  <div class="banner">
    <svg viewBox="0 0 1106 541" xmlns="http://www.w3.org/2000/svg">
      <defs>
        <linearGradient id="grass" x1="0" y1="0" x2="1" y2="1"><stop offset="0" stop-color="var(--grass-a)"/><stop offset="1" stop-color="var(--grass-b)"/></linearGradient>
        <linearGradient id="meter" x1="0" y1="0" x2="1" y2="1"><stop offset="0" stop-color="var(--meter-b)"/><stop offset="0.5" stop-color="var(--meter-a)"/><stop offset="1" stop-color="#eeeeee"/></linearGradient>
        <linearGradient id="fire" x1="0" y1="0" x2="1" y2="1"><stop offset="0" stop-color="var(--fire-b)"/><stop offset="0.45" stop-color="var(--fire-a)"/><stop offset="1" stop-color="var(--fire-b)"/></linearGradient>
        <linearGradient id="tools" x1="0" y1="0" x2="1" y2="1"><stop offset="0" stop-color="#eeeeee"/><stop offset="0.5" stop-color="var(--tools-a)"/><stop offset="1" stop-color="var(--tools-b)"/></linearGradient>
        <linearGradient id="hands" x1="0" y1="0" x2="1" y2="1"><stop offset="0" stop-color="var(--hands-b)"/><stop offset="1" stop-color="var(--hands-a)"/></linearGradient>
        <linearGradient id="portrait" x1="0" y1="0" x2="0" y2="1"><stop offset="0" stop-color="var(--portrait-a)"/><stop offset="1" stop-color="var(--portrait-b)"/></linearGradient>
      </defs>

      <g class="contact-block">
        <polygon role="img" aria-label="Portrait photo of the inspector in a hard hat and safety vest" fill="url(#portrait)" points="114,44 194,124 114,204 33,124"/>
        <text class="name" x="210" y="114" textLength="297" lengthAdjust="spacingAndGlyphs">YOUR NAME</text>
        <line x1="212" y1="124" x2="537" y2="124" stroke="var(--rule-grey)" stroke-width="3"/>
        <text class="contact" x="219" y="150" textLength="171" lengthAdjust="spacingAndGlyphs">Call&#160; 8888 8888 88</text>
        <text class="contact" x="219" y="173" textLength="257" lengthAdjust="spacingAndGlyphs">Email&#160; yourname@info.com</text>
      </g>

      <g class="collage">
        <polygon fill="var(--brand-red)" points="164,541 705,0 1106,0 1106,541"/>
        <polygon fill="var(--ink-black)" points="839,0 1104,0 972,132"/>
        <polygon fill="var(--ink-black)" points="1106,270 1106,538 972,404"/>
        <polygon class="tile" role="img" aria-label="Photo of a digital multimeter and electrical parts" fill="url(#meter)" points="839,0 1106,267 969,404 704,137"/>
        <polygon class="tile" role="img" aria-label="Photo of a magnifying glass and house keys on grass" fill="url(#grass)" points="704,137 834,271 699,406 566,273"/>
        <polygon class="tile" role="img" aria-label="Photo of a wood burning stove with fire" fill="url(#fire)" points="566,273 699,406 564,541 432,407"/>
        <polygon class="tile" role="img" aria-label="Photo of electrician tools, pliers and screwdrivers" fill="url(#tools)" points="834,271 969,404 834,541 699,406"/>
        <polygon class="tile" role="img" aria-label="Photo of hands working on a fireplace installation" fill="url(#hands)" points="699,406 834,541 699,676 564,541"/>
      </g>

      <text class="slogan" x="291" y="530" textLength="720" lengthAdjust="spacingAndGlyphs" transform="rotate(-45 291 530)">THE BEST IN TOWN</text>
    </svg>
  </div>
</body>
</html>
```